DORV2020 Save the date post card

Take the look and feel of the logo you designed and create a save the date postcard. 7L" by 5"H - print ready file with crop marks and bleeds.

Colors

Designer to choose colors to be used in the design.

Requirements
Must have
• The logo somewhere on the card.
• The following text:
• Save the Date
• June 1 - 4
• dorvsummit.ca
• Stronger United: Gather. Spark. Flourish.
Nice to have
• The following text:
• Vision: The vision of the DORV 2020 conference is to improve patient care by bringing together the Canadian Emergency Medicine community.
• Learning Objectives:
• By the end of the conference, delegates will be able to;
• • Apply up to date evidence to inform clinical decisions;
• • Acquire practical skills by participating in interactive sessions;
• • Connect and collaborate with other delegates;
• • Consider strategies to ensure career longevity; and
• • Influence the future direction of Emergency Medicine in Canada

```html
<!DOCTYPE html>
<html lang="en">
<head>
<meta charset="utf-8">
<title>DORV2020 Save the Date Postcard</title>
<link href="https://fonts.googleapis.com/css2?family=Montserrat:wght@400;600;700;800&display=swap" rel="stylesheet">
<style>
  :root{
    --sky:#2e9fdc;
    --sky-light:#5cb8ea;
    --sky-deep:#1e86c6;
    --red:#e2232a;
    --white:#ffffff;
    --paper:#e4e4e4;
    --ink-line:#9a9a9a;
    --brand:#7a3fb0;
  }
  *{box-sizing:border-box;margin:0;padding:0}
  html,body{width:1200px;height:800px;overflow:hidden}
  body{background:var(--paper);font-family:"Montserrat",Arial,sans-serif;position:relative}
  .postcard{position:absolute;top:200px;width:560px;height:400px;overflow:hidden;background:var(--white);box-shadow:0 2px 8px rgba(0,0,0,.12)}
  .postcard--front{left:27px}
  .postcard--back{left:613px}
  .postcard__art{position:absolute;inset:0;width:100%;height:100%}

  /* front */
  .headline{position:absolute;left:30px;top:78px;color:var(--white);font-weight:800;font-size:37px;letter-spacing:.3px;line-height:1;white-space:nowrap}
  .date-tag{position:absolute;left:46px;top:126px;background:var(--red);color:var(--white);font-weight:700;font-size:13px;padding:3px 12px;border:1px solid var(--white)}
  .brand{position:absolute;left:34px;top:334px;display:flex;align-items:center;gap:8px;color:var(--brand);font-weight:800;font-size:26px}
  .brand__dot{width:14px;height:14px;border-radius:50%;background:var(--brand)}
  .tagline{position:absolute;right:24px;top:338px;width:240px;text-align:center;color:var(--sky);font-size:11.5px;font-weight:400;padding:5px 0;border-top:1px solid var(--sky);border-bottom:1px solid var(--sky)}

  /* back */
  .message{position:absolute;left:22px;top:34px;width:300px;color:var(--white)}
  .message__vision{font-size:11px;font-weight:600;line-height:1.35}
  .message__heading{font-size:18px;font-weight:700;margin-top:12px}
  .message__intro{font-size:11px;font-weight:600;line-height:1.35;margin-top:3px}
  .message__list{list-style:disc;padding-left:16px;margin-top:4px}
  .message__list li{font-size:11px;line-height:1.35;margin-bottom:3px}
  .address-panel{position:absolute;left:340px;top:22px;width:200px;height:258px;background:var(--white)}
  .stamp{position:absolute;right:16px;top:16px;width:52px;height:56px;border:1px solid var(--ink-line)}
  .address-lines{position:absolute;left:18px;right:16px;top:98px}
  .address-lines span{display:block;height:24px;border-bottom:1px solid var(--ink-line)}
  .website{position:absolute;left:0;right:0;bottom:18px;text-align:center;color:var(--sky);font-size:12px}
</style>
</head>
<body>

<section class="postcard postcard--front" aria-label="Postcard front">
  <svg class="postcard__art" viewBox="0 0 560 400">
    <defs>
      <linearGradient id="skyline" x1="0" y1="0" x2="0" y2="1">
        <stop offset="0" stop-color="#5cb8ea"/>
        <stop offset="1" stop-color="#2e9fdc"/>
      </linearGradient>
      <linearGradient id="speakerPhoto" x1="0" y1="0" x2="1" y2="1">
        <stop offset="0" stop-color="#c9c3be"/>
        <stop offset="1" stop-color="#3a3430"/>
      </linearGradient>
      <linearGradient id="networkPhoto" x1="0" y1="0" x2="1" y2="1">
        <stop offset="0" stop-color="#6b5a4c"/>
        <stop offset="1" stop-color="#2a2522"/>
      </linearGradient>
    </defs>
    <rect width="560" height="400" fill="url(#skyline)" role="img" aria-label="Faded blue city skyline with parliament towers"/>
    <path d="M0 400 L0 318 C120 250 300 222 560 212 L560 400 Z" fill="#ffffff"/>
    <path d="M0 322 C90 268 160 246 230 232" fill="none" stroke="#e2232a" stroke-width="4"/>
    <circle cx="458" cy="126" r="94" fill="#ffffff"/>
    <circle cx="458" cy="126" r="88" fill="url(#networkPhoto)" stroke="#2e9fdc" stroke-width="7" role="img" aria-label="Photo of delegates networking at a reception"/>
    <circle cx="298" cy="234" r="90" fill="#ffffff"/>
    <circle cx="298" cy="234" r="84" fill="url(#speakerPhoto)" stroke="#2e9fdc" stroke-width="7" role="img" aria-label="Photo of a speaker at a podium"/>
  </svg>
  <h1 class="headline">SAVE THE DATE</h1>
  <p class="date-tag">June 1 - 4</p>
  <div class="brand"><span class="brand__dot"></span>DORV2020</div>
  <p class="tagline">Stronger United: Gather. Spark. Flourish.</p>
</section>

<section class="postcard postcard--back" aria-label="Postcard back">
  <svg class="postcard__art" viewBox="0 0 560 400">
    <defs>
      <linearGradient id="skylineBack" x1="0" y1="0" x2="0" y2="1">
        <stop offset="0" stop-color="#2e9fdc"/>
        <stop offset="1" stop-color="#5cb8ea"/>
      </linearGradient>
    </defs>
    <rect width="560" height="400" fill="url(#skylineBack)" role="img" aria-label="Faded blue city skyline"/>
    <path d="M0 400 L0 388 C130 320 330 282 560 296 L560 400 Z" fill="#ffffff"/>
    <path d="M0 384 C60 352 120 330 180 314" fill="none" stroke="#e2232a" stroke-width="4"/>
  </svg>
  <div class="message">
    <p class="message__vision">Vision: The vision of the DORV 2020 conference is to improve patient care by bringing together the Canadian Emergency Medicine community.</p>
    <h2 class="message__heading">Learning Objectives:</h2>
    <p class="message__intro">By the end of the conference, delegates will be able to:</p>
    <ul class="message__list">
      <li>Apply up to date evidence to inform clinical decisions;</li>
      <li>Acquire practical skills by participating in interactive sessions;</li>
      <li>Connect and collaborate with other delegates;</li>
      <li>Consider strategies to ensure career longevity; and</li>
      <li>Influence the future direction of Emergency Medicine in Canada</li>
    </ul>
  </div>
  <div class="address-panel">
    <div class="stamp"></div>
    <div class="address-lines"><span></span><span></span><span></span><span></span><span></span></div>
    <p class="website">dorvsummit.ca</p>
  </div>
</section>

</body>
</html>
```